Honey Packaging Label Design

The honey packaging label should be designed in a transparent look. The design concept for this product should be natural and healthy. Please include the logo and nutrition fact in the attachment. The size for the label is 9cm width by 5cm height. Please also include the information of our company. Since the bar code is not ready yet, please leave space for the bar code.
Velmora International Trading Group Inc.
#2487 - 736 Thistlebrook St., Vancouver, V5K 2R8
Tel: 1-604-820-3147/3146
Since our company's logo for the packaging is still not finished yet, so please leave space for our logo, and we will be able to add it on later.

Please be creative.

If you have any question you can call at 1-604-820-3147/3146 or e-mail to marthak@velmora-example.ca

Thank you!

Target Market(s)

Supermarket, wholesale

Industry/Entity Type

Product

Requirements
Must have
• Nutrition facts, bar code, logo, address, transparent, modern look design, geometry design.
Nice to have
• Bees, flowers
Should not have
• Traditional design.

```html
<!DOCTYPE html>
<html lang="en">
<head>
<meta charset="utf-8">
<title>Honey Label — Canadian White Honey</title>
<link rel="stylesheet" href="https://fonts.googleapis.com/css2?family=Didact+Gothic&family=Alegreya+Sans+SC:wght@400;500;700&display=swap">
<style>
  :root {
    --page-bg: #f1f1f1;
    --label-bg: #f6f6f6;
    --hex-fill: #dcdcdc;
    --brown: #5b2f1b;
    --orange: #f4a52a;
    --orange-text: #ee9e2c;
    --ink: #3d2416;
    --white: #ffffff;
  }
  * { box-sizing: border-box; margin: 0; padding: 0; }
  html, body { width: 1200px; height: 921px; overflow: hidden; background: var(--page-bg); }
  .canvas { position: relative; width: 1200px; height: 921px; }
  .label {
    position: absolute; left: 100px; top: 182px; width: 1000px; height: 556px;
    background: var(--label-bg);
  }
  .label-shapes { position: absolute; inset: 0; }

  .product-mark { position: absolute; left: 216px; top: 88px; width: 96px; height: 52px; }
  .product-name {
    position: absolute; left: 60px; width: 400px; top: 184px;
    font-family: "Didact Gothic", sans-serif; font-size: 80px; letter-spacing: 2px;
    color: var(--white); line-height: 1; text-align: center; font-weight: 400;
    text-shadow: 0 1px 3px rgba(60,36,22,0.22);
  }
  .product-tagline {
    position: absolute; left: 60px; width: 400px; top: 276px;
    display: flex; align-items: center; justify-content: center; gap: 10px;
    font-family: "Didact Gothic", sans-serif; font-size: 16px; color: var(--white);
    letter-spacing: 0.5px; text-shadow: 0 1px 2px rgba(60,36,22,0.25);
  }
  .dots { display: flex; gap: 4px; }
  .dots i { width: 7px; height: 7px; border-radius: 50%; background: var(--orange); display: block; }
  .flower { position: absolute; left: 206px; top: 340px; width: 120px; height: 120px; }

  .back-text {
    position: absolute; left: 560px; width: 256px; top: 66px;
    font-family: "Alegreya Sans SC", sans-serif; color: var(--ink); text-align: center;
  }
  .logo-space {
    font-family: "Didact Gothic", sans-serif; color: var(--orange-text);
    font-size: 20px; line-height: 24px; font-weight: 700; letter-spacing: 1px;
  }
  .nutrition-title { margin-top: 6px; font-size: 16px; font-weight: 700; line-height: 20px; white-space: nowrap; }
  .nutrition-row { font-size: 17px; line-height: 21px; white-space: nowrap; }
  .nutrition-row.serving { font-size: 12px; line-height: 18px; }
  .nutrition-note {
    position: absolute; left: 586px; width: 224px; top: 346px;
    font-family: "Alegreya Sans SC", sans-serif; font-size: 11px; line-height: 13px;
    color: var(--ink); text-align: center;
  }
  .company-info {
    position: absolute; left: 614px; width: 210px; top: 424px;
    font-family: "Alegreya Sans SC", sans-serif; font-size: 10px; line-height: 12px;
    color: var(--orange-text); text-align: center; font-weight: 500;
  }
  .barcode-space {
    position: absolute; left: 820px; top: 108px; width: 46px; height: 340px;
    display: flex; align-items: center; justify-content: center;
  }
  .barcode-space span {
    transform: rotate(-90deg); white-space: nowrap;
    font-family: "Didact Gothic", sans-serif; font-weight: 700; font-size: 18px;
    letter-spacing: 1px; color: var(--brown);
  }
</style>
</head>
<body>
<main class="canvas">
  <section class="label">
    <svg class="label-shapes" viewBox="0 0 1000 556" width="1000" height="556">
      <polygon points="28,278 150,12 390,12 500,278 390,544 150,544" fill="var(--hex-fill)" stroke="var(--brown)" stroke-width="12" stroke-linejoin="round"/>
      <polygon points="48,278 162,30 378,30 482,278 378,526 162,526" fill="none" stroke="var(--orange)" stroke-width="3"/>
      <polygon points="500,278 610,12 850,12 972,278 850,544 610,544" fill="var(--hex-fill)" stroke="var(--brown)" stroke-width="12" stroke-linejoin="round"/>
      <polygon points="518,278 622,30 838,30 954,278 838,526 622,526" fill="none" stroke="var(--orange)" stroke-width="3"/>
      <rect class="barcode-band" x="820" y="108" width="46" height="340" fill="var(--orange)"/>
    </svg>

    <div class="front">
      <div class="product-mark" role="img" aria-label="Product mark: bee wing above a curved line" style="border-radius: 50%; background: var(--orange);"></div>
      <h1 class="product-name">HONEY</h1>
      <p class="product-tagline"><span class="dots"><i></i><i></i><i></i></span>Canadian White Honey<span class="dots"><i></i><i></i><i></i></span></p>
      <div class="flower" role="img" aria-label="Orange daisy flower with a green centre" style="border-radius: 50%; background: radial-gradient(circle, #2e9b4a 0 8%, var(--orange) 9% 55%, transparent 72%);"></div>
    </div>

    <div class="back">
      <div class="back-text">
        <p class="logo-space">COMPANY<br>LOGO</p>
        <p class="nutrition-title">Nutrition Fact / Valeur nutritive</p>
        <p class="nutrition-row serving">Per 1 tablespoon (20 g) / Pour 1 cuillère à table (20 g)</p>
        <p class="nutrition-row">Amount - % Daily Values</p>
        <p class="nutrition-row">Teneur - % valeur quotidienne</p>
        <p class="nutrition-row">Calories / Calories 60</p>
        <p class="nutrition-row">Fat / Lipides 0 g - 0 %</p>
        <p class="nutrition-row">Carbohydrate / Glucides 17 g - 6%</p>
        <p class="nutrition-row">Sugars / Sucres 16 g</p>
        <p class="nutrition-row">Protein / Protéines 0 g</p>
      </div>
      <p class="nutrition-note">Not a significant source of saturated fat, trans fat, cholesterol, sodium, fibres, vitamin A, vitamin C, calcium or iron. / Source négligeable de lipides saturés, lipides trans, cholestérol, sodium, fibres, vitamine A, vitamine C, calcium et fer.</p>
      <p class="company-info">Velmora International Trading Group Inc.<br>#2487 - 736 Thistlebrook St., Vancouver, V5K 2R8<br>1-604-820-3147/3146</p>
      <div class="barcode-space"><span>BAR CODE</span></div>
    </div>
  </section>
</main>
</body>
</html>
```